Brightwell cleaning and maintenance company

An expansive website whereby we can advertise our commercial cleaning and maintenance services across a service portfolio of commercial cleaning and property maintenance. Whereby potential skilled resources can deposit there resume so we can collaborate and match candidates to a broad range of cleaning and maintenance jobs/projects.
Updates

Looking for more extensive ideas so the front page can change pictures on it with the focus for Brightwell Commercial Cleaning and Maintenance. Also need to bring in all the portfolios we offer including 1. Equipment Cleaning and Sanitisation Services 2. High pressure gurney and play ground equipment cleaning 3. General Cleaning and Property Facilities Management 4. Project and Recruiting Services, to allow for potential professional cleaners, handy man, mechanics, warehousing resources , electricians to deposit there resume. Most of the designers have stuck with the old portfolio categories , however the portfolio of services we offer has been updated so that needs to be reflected in the website. Also not necessary to use all my original photos I would like the opening page of the website to perhaps be able to change and have different pictures is that possible thank you

Coding

```html
<!DOCTYPE html>
<html lang="en">
<head>
<meta charset="utf-8">
<title>Brightwell — Commercial Cleaning &amp; Maintenance</title>
<link href="https://fonts.googleapis.com/css2?family=Lato:wght@400;700;900&family=Lora:wght@700&display=swap" rel="stylesheet">
<style>
:root{
  --orange:#f63d0c;
  --navy:#0c2a63;
  --pale:#eef3f8;
  --ink:#333a44;
  --muted:#6a717b;
  --white:#ffffff;
}
*{box-sizing:border-box;margin:0;padding:0}
html,body{width:1200px;height:4107px;overflow:hidden}
body{font-family:'Lato',sans-serif;color:var(--ink);background:var(--white);position:relative}
.hl{color:var(--orange)}
.dk{color:var(--navy)}

/* header */
.topbar{position:absolute;top:0;left:0;width:1200px;height:99px;border-top:3px solid var(--navy)}
.brand{position:absolute;left:143px;top:20px;display:flex;align-items:center;gap:12px}
.brand-dot{width:44px;height:44px;border-radius:50%;background:var(--navy)}
.brand-name{font-family:'Lora',serif;font-weight:700;font-size:44px;color:var(--orange);line-height:1}
.phone{position:absolute;left:574px;top:26px;display:flex;align-items:center;gap:12px;font-weight:900;font-size:30px;color:var(--navy)}
.phone-ring{width:40px;height:40px;border:2px solid var(--orange);border-radius:50%;display:flex;align-items:center;justify-content:center}
.social-top{position:absolute;left:869px;top:27px;display:flex;gap:8px}
.social-top span{width:41px;height:41px;border:2px solid var(--orange);border-radius:50%}
.mainnav{position:absolute;top:99px;left:0;width:1200px;height:48px;background:var(--orange);display:flex;padding-left:145px}
.mainnav a{color:var(--white);text-decoration:none;font-size:15px;font-weight:700;line-height:48px;padding:0 14px;text-transform:uppercase}
.mainnav a.active{background:var(--navy)}

/* hero */
.hero{position:absolute;top:147px;left:0;width:1200px;height:660px;overflow:hidden}
.hero-photo{position:absolute;inset:0;background:linear-gradient(110deg,#6e4a2c 0%,#b57a46 35%,#c99562 55%,#8c7255 80%,#5a4c40 100%)}
.hero-title{position:absolute;left:143px;top:140px;font-family:'Lora',serif;font-weight:700;font-size:86px;color:var(--white);line-height:1}
.hero-sub{position:absolute;left:144px;top:274px;font-size:21px;font-weight:700;color:var(--white);line-height:31px}
.btn{display:inline-block;color:var(--white);font-size:16px;font-weight:700;text-transform:uppercase;text-decoration:none}
.hero .btn{position:absolute;left:143px;top:371px;width:171px;height:49px;line-height:49px;text-align:center;background:var(--navy)}
.arrow{position:absolute;top:269px;width:38px;height:38px;border-radius:50%;background:#2a2622;display:flex;align-items:center;justify-content:center}
.dots{position:absolute;top:494px;left:554px;display:flex;gap:8px}
.dots span{width:11px;height:11px;border-radius:50%;background:var(--white)}
.dots span.on{background:transparent;border:2px solid var(--white)}
.hero-curve{position:absolute;left:0;bottom:0}

/* services */
.h2{position:absolute;left:0;width:1200px;text-align:center;font-family:'Lora',serif;font-weight:700;font-size:50px;line-height:1}
.services{position:absolute;top:953px;left:143px;width:914px;display:grid;grid-template-columns:442px 442px;column-gap:30px;row-gap:32px}
.svc-photo{height:296px}
.svc-label{height:61px;line-height:61px;text-align:center;color:var(--white);font-weight:700;font-size:24px;white-space:nowrap}
.svc-label.o{background:var(--orange)}
.svc-label.n{background:var(--navy)}

/* working */
.working{position:absolute;top:1801px;left:0;width:1200px;height:800px;background:var(--pale)}
.lead{position:absolute;top:183px;width:1200px;text-align:center;font-size:18px;color:#4d545d}
.body-copy{position:absolute;top:246px;left:180px;width:840px;text-align:center;font-size:18px;line-height:31px;color:#4d545d}
.pillars{position:absolute;top:404px;left:143px;display:flex;gap:25px}
.pillar{width:289px;height:293px;background:var(--white);box-shadow:0 1px 4px rgba(0,0,0,.08);text-align:center;padding-top:42px}
.pillar svg{display:block;margin:0 auto}
.pillar h3{font-size:15px;font-weight:900;color:#222;margin-top:14px}
.pillar .rule{width:32px;height:3px;background:var(--orange);margin:14px auto 16px}
.pillar p{font-size:12.5px;line-height:17px;color:var(--muted);width:200px;margin:0 auto}

/* gallery */
.about{position:absolute;top:2601px;left:0;width:1200px;height:1000px}
.gallery{position:absolute;top:192px;left:8px;display:grid;grid-template-columns:repeat(4,289px);grid-auto-rows:265px;gap:8px 9px}
.about .btn{position:absolute;left:515px;top:770px;width:169px;height:47px;line-height:47px;text-align:center;background:var(--orange)}

/* newsletter */
.mark{position:absolute;width:30px;height:30px;border-radius:50%;background:var(--navy)}
.signup{position:absolute;top:3806px;left:223px;display:flex;gap:16px}
.signup input{width:301px;height:39px;border:1px solid #dcdfe3;padding-left:20px;font-family:'Lato',sans-serif;font-size:12px;color:#555}
.signup button{width:121px;height:39px;background:var(--orange);border:0;color:var(--white);font-family:'Lato',sans-serif;font-weight:700;font-size:16px;text-transform:uppercase}
.social-foot{position:absolute;top:3899px;left:489px;display:flex;gap:7px}
.social-foot span{width:48px;height:48px;border:2px solid var(--orange);border-radius:50%}
.footnav{position:absolute;top:3987px;left:0;width:1200px;display:flex;justify-content:center;gap:33px}
.footnav a{color:#222;text-decoration:none;font-size:17px;text-transform:uppercase}
.copy{position:absolute;top:4043px;left:0;width:1200px;text-align:center;font-size:12.5px;color:#666}
</style>
</head>
<body>

<header class="topbar">
  <div class="brand"><span class="brand-dot"></span><span class="brand-name">Brightwell</span></div>
  <div class="phone">
    <span class="phone-ring">
      <svg width="22" height="22" viewBox="0 0 24 24"><path d="M6.6 10.8a15 15 0 0 0 6.6 6.6l2.2-2.2c.3-.3.7-.4 1-.2 1.1.4 2.3.6 3.6.6.6 0 1 .4 1 1V20c0 .6-.4 1-1 1C10.6 21 3 13.4 3 4c0-.6.4-1 1-1h3.5c.6 0 1 .4 1 1 0 1.3.2 2.5.6 3.6.1.3 0 .7-.2 1z" fill="var(--orange)"/></svg>
    </span>
    (07) 3900 1275
  </div>
  <div class="social-top"><span></span><span></span><span></span><span></span></div>
</header>

<nav class="mainnav">
  <a class="active" href="#">Home</a><a href="#">Services</a><a href="#">About Us</a><a href="#">Our People</a><a href="#">Safety &amp; Compliance</a><a href="#">Contact</a>
</nav>

<section class="hero">
  <div class="hero-photo" role="img" aria-label="Worker cleaning paving with a high pressure water lance"></div>
  <h1 class="hero-title">Brightwell</h1>
  <p class="hero-sub">Sed ut perspiciatis unde omnis iste natus error<br>sit voluptatem accusantium</p>
  <a class="btn" href="#">Get Started ➔</a>
  <span class="arrow" style="left:52px"><svg width="14" height="14" viewBox="0 0 14 14"><path d="M9 2 4 7l5 5" stroke="#fff" stroke-width="2" fill="none"/></svg></span>
  <span class="arrow" style="left:1110px"><svg width="14" height="14" viewBox="0 0 14 14"><path d="M5 2l5 5-5 5" stroke="#fff" stroke-width="2" fill="none"/></svg></span>
  <div class="dots"><span></span><span></span><span class="on"></span><span></span><span></span></div>
  <svg class="hero-curve" width="1200" height="120" viewBox="0 0 1200 120">
    <path d="M0 120 L0 98 Q300 70 600 20 Q900 70 1200 98 L1200 120 Z" fill="#fff"/>
    <path d="M0 98 Q300 70 600 20 Q900 70 1200 98" stroke="var(--orange)" stroke-width="5" fill="none"/>
  </svg>
</section>
<span class="mark" style="left:585px;top:738px"></span>

<h2 class="h2" style="top:838px"><span class="hl">Our</span> <span class="dk">Services</span></h2>
<div class="services">
  <article><div class="svc-photo" role="img" aria-label="Food service machine being cleaned and sanitised" style="background:linear-gradient(135deg,#d9d6d3,#9aa3a8 55%,#6ab4bf)"></div><div class="svc-label o">Equipment Sanitisation Services</div></article>
  <article><div class="svc-photo" role="img" aria-label="High pressure cleaning of colourful playground equipment" style="background:linear-gradient(135deg,#8aa67a,#5d6f8e 50%,#c8415a)"></div><div class="svc-label n">Pressure &amp; Playground Cleaning</div></article>
  <article><div class="svc-photo" role="img" aria-label="Clean stainless steel commercial premises" style="background:linear-gradient(135deg,#d8d8d6,#8d8f90 50%,#5a5650)"></div><div class="svc-label n">General Cleaning &amp; Facilities</div></article>
  <article><div class="svc-photo" role="img" aria-label="Skilled trades worker on a maintenance project" style="background:linear-gradient(135deg,#5a5652,#7f7c78 50%,#b0b0ae)"></div><div class="svc-label o">Project &amp; Recruiting Services</div></article>
</div>

<section class="working">
  <h2 class="h2" style="top:106px"><span class="hl">Working With</span> <span class="dk">Brightwell</span></h2>
  <p class="lead">We are Brightwell, a leading Australian cleaning and maintenance company.</p>
  <p class="body-copy">From equipment sanitisation and high pressure cleaning to property facilities management, our team keeps every site safe and spotless. We also match skilled cleaners, handymen, mechanics, warehousing staff and electricians to projects, so send us your resume.</p>
  <div class="pillars">
    <div class="pillar">
      <svg width="58" height="58" viewBox="0 0 58 58"><circle cx="29" cy="29" r="26" stroke="var(--navy)" stroke-width="5" fill="none"/><circle cx="29" cy="29" r="16" stroke="var(--navy)" stroke-width="5" fill="none"/><circle cx="29" cy="29" r="7" fill="var(--navy)"/></svg>
      <h3>OUR PURPOSE</h3><div class="rule"></div>
      <p>Sed ut perspiciatis unde omnis iste natus error sit volupt atem accusa ntium doloremque laudan tium totam rem aperiam</p>
    </div>
    <div class="pillar">
      <svg width="66" height="58" viewBox="0 0 66 58"><path d="M2 29 Q33 -4 64 29 Q33 62 2 29 Z" fill="var(--navy)"/><circle cx="33" cy="29" r="13" fill="#fff"/><circle cx="33" cy="29" r="8" fill="var(--navy)"/></svg>
      <h3>OUR VISION</h3><div class="rule"></div>
      <p>Sed ut perspiciatis unde omnis iste natus error sit volupt atem accusa ntium doloremque laudan tium totam rem aperiam</p>
    </div>
    <div class="pillar">
      <svg width="62" height="58" viewBox="0 0 62 58"><path d="M3 4 V54 H60" stroke="var(--navy)" stroke-width="5" fill="none"/><path d="M12 44 L26 28 L36 36 L54 14" stroke="var(--navy)" stroke-width="5" fill="none"/><path d="M44 12 H56 V24" stroke="var(--navy)" stroke-width="5" fill="none"/></svg>
      <h3>OUR STRATEGY</h3><div class="rule"></div>
      <p>Sed ut perspiciatis unde omnis iste natus error sit volupt atem accusa ntium doloremque laudan tium totam rem aperiam</p>
    </div>
  </div>
</section>

<section class="about">
  <svg style="position:absolute;left:0;top:0" width="1200" height="1000" viewBox="0 0 1200 1000">
    <path d="M0 0 H1200 V906 Q900 920 600 994 Q300 920 0 906 Z" fill="var(--navy)"/>
    <path d="M0 914 Q300 930 600 1000 Q900 930 1200 914" stroke="var(--orange)" stroke-width="6" fill="none"/>
  </svg>
  <h2 class="h2" style="top:90px"><span class="hl">We Are</span> <span style="color:#fff">Brightwell</span></h2>
  <div class="gallery">
    <div role="img" aria-label="Slushie machine bowls after cleaning" style="background:linear-gradient(135deg,#6f8fa3,#c9d3d8 50%,#8aa0ad)"></div>
    <div role="img" aria-label="Coffee machine drip tray cleaned" style="background:linear-gradient(135deg,#cfcfcd,#3a3a3c 55%,#9a9a98)"></div>
    <div role="img" aria-label="Disassembled machine parts laid out for sanitising" style="background:linear-gradient(135deg,#8c8e90,#2f3336 50%,#c9a13a)"></div>
    <div role="img" aria-label="Stainless steel tray after cleaning" style="background:linear-gradient(135deg,#b8b6b2,#7a7874 50%,#d6d4cf)"></div>
    <div role="img" aria-label="Machine hopper with dasher part" style="background:linear-gradient(135deg,#8d8e8c,#c4c4c2 45%,#c2322c 70%,#9d9c99)"></div>
    <div role="img" aria-label="Freezer cylinder and beater blade" style="background:linear-gradient(135deg,#ece8e2,#a39c92 50%,#2e2b27)"></div>
    <div role="img" aria-label="Dispenser tray being cleaned" style="background:linear-gradient(135deg,#5d6064,#1e2024 50%,#c9ccce)"></div>
    <div role="img" aria-label="Machine interior with cleaning bucket" style="background:linear-gradient(135deg,#4a4845,#9b9893 50%,#ecebe8)"></div>
  </div>
  <a class="btn" href="#">View More ➔</a>
</section>

<span class="mark" style="left:585px;top:3640px"></span>
<h2 class="h2" style="top:3704px"><span class="hl">Subscribe To</span> <span class="dk">Our Newsletter</span></h2>
<form class="signup">
  <input type="text" placeholder="Full Name">
  <input type="email" placeholder="Email Address">
  <button type="button">Submit</button>
</form>
<div class="social-foot"><span></span><span></span><span></span><span></span></div>
<nav class="footnav"><a href="#">Home</a><a href="#">Services</a><a href="#">About Us</a><a href="#">Our People</a><a href="#">Safety &amp; Compliance</a><a href="#">Contact</a></nav>
<p class="copy">© 2020 Brightwell . All rights reserved &nbsp;| &nbsp;Privacy Policy</p>

</body>
</html>
```